Clean business card with logo provided

I want a card that will stand out among the masses. I need the color and image to show professionalism and yet have a family appeal showing that I only deal with win/win scenarios. The back of the card will be used to take notes about the individual so I can use that in my database entry. I like modern design but need professionalism in it also. It needs to fit my "clean, safe, and affordable housing" motto. I need to be able to write on the file and update the card details for my employees.

Target Market(s)

Investors looking to make investment income through real estate

Industry/Entity Type

Real Estate

Contact Information for Business Card

Mark Dunthorpe
blank address, city, st, zip code
480-555-3174
markdunthorpe@brivoholdings.example
www.brivoholdings.example

Font styles to use
Sans Serif

Requirements
Must have
• I would like the back of the card to have lines for info. example
• Met/Visited: Date:
• Interets:
Nice to have
• I want the cards color to match the logo background color. Font with details to be san serif and black. I want the card rectangular with square corners. Standard business card size. I would like to see cards designed with both images to see which i prefer more.

```html
<!DOCTYPE html>
<html lang="en">
<head>
<meta charset="utf-8">
<title>Quennick Leasing LLC – Business Card</title>
<link href="https://fonts.googleapis.com/css2?family=Open+Sans:wght@400;600;700&display=swap" rel="stylesheet">
<style>
  :root {
    --card-cyan: #19bfd4;
    --ink: #0d1b20;
    --rule: #ffffff;
    --brand: #ffffff;
    --backdrop: #eef1f2;
  }
  * { box-sizing: border-box; margin: 0; padding: 0; }
  html, body { width: 1200px; height: 900px; overflow: hidden; }
  body {
    background: var(--backdrop);
    font-family: "Open Sans", Arial, sans-serif;
    color: var(--ink);
    position: relative;
  }
  .card {
    position: absolute;
    left: 285px;
    width: 630px;
    height: 360px;
    background: var(--card-cyan);
    box-shadow: 0 6px 18px rgba(0,0,0,0.18);
  }
  .card-back { top: 50px; }
  .card-front { top: 470px; }

  /* Back: note lines */
  .note-form { position: absolute; left: 48px; top: 64px; width: 540px; }
  .note-row { display: flex; align-items: flex-end; margin-bottom: 24px; }
  .note-label { font-weight: 700; font-size: 16px; line-height: 20px; white-space: nowrap; margin-right: 10px; }
  .note-line { flex: 1; border-bottom: 1.5px solid var(--rule); height: 18px; }
  .note-line.short { flex: 0 0 190px; margin-right: 18px; }
  .back-brand {
    position: absolute; right: 48px; top: 222px;
    display: flex; align-items: center; gap: 10px;
  }
  .back-brand .brand-name { font-size: 18px; letter-spacing: 2px; }
  .back-brand .brand-mark { width: 16px; height: 16px; }

  /* Shared brand lockup */
  .brand-name {
    font-weight: 600; color: var(--brand); white-space: nowrap; line-height: 1;
  }
  .brand-mark { border-radius: 50%; background: var(--ink); flex: none; }

  /* Front */
  .front-brand {
    position: absolute; left: 0; right: 0; top: 72px;
    display: flex; justify-content: center; align-items: center; gap: 16px;
  }
  .front-brand .brand-name { font-size: 34px; letter-spacing: 4px; }
  .front-brand .brand-mark { width: 28px; height: 28px; }

  .contact { position: absolute; left: 0; right: 0; top: 180px; text-align: center; }
  .person { font-size: 20px; font-weight: 700; line-height: 26px; margin-bottom: 10px; }
  .person .role { font-weight: 600; }
  .person .sep { margin: 0 10px; }
  .contact-line {
    font-size: 18px; font-weight: 600; line-height: 24px; margin-bottom: 6px;
    display: flex; justify-content: center; align-items: center; gap: 8px;
  }
  .contact-line svg { width: 16px; height: 16px; flex: none; }
  .contact-line .gap { width: 20px; }
</style>
</head>
<body>
  <section class="card card-back" aria-label="Card back: notes">
    <div class="note-form">
      <div class="note-row">
        <span class="note-label">Met/Visited:</span>
        <span class="note-line short"></span>
        <span class="note-label">Date:</span>
        <span class="note-line"></span>
      </div>
      <div class="note-row">
        <span class="note-label">Interets:</span>
        <span class="note-line"></span>
      </div>
      <div class="note-row">
        <span class="note-label">Problems:</span>
        <span class="note-line"></span>
      </div>
    </div>
    <div class="back-brand">
      <span class="brand-name">QUENNICK LEASING LLC</span>
      <span class="brand-mark"></span>
    </div>
  </section>

  <section class="card card-front" aria-label="Card front: contact details">
    <div class="front-brand">
      <span class="brand-name">QUENNICK LEASING LLC</span>
      <span class="brand-mark"></span>
    </div>
    <div class="contact">
      <p class="person">Mark Dunthorpe<span class="sep">•</span><span class="role">Manager</span></p>
      <p class="contact-line">
        <svg viewBox="0 0 24 24" aria-hidden="true"><path fill="#0d1b20" d="M6.6 10.8a15 15 0 0 0 6.6 6.6l2.2-2.2c.3-.3.7-.4 1-.2 1.1.4 2.3.6 3.6.6.6 0 1 .4 1 1V20c0 .6-.4 1-1 1A17 17 0 0 1 3 4c0-.6.4-1 1-1h3.5c.6 0 1 .4 1 1 0 1.3.2 2.5.6 3.6.1.3 0 .7-.2 1z"/></svg>
        <span>480-555-3174</span>
        <span class="gap"></span>
        <svg viewBox="0 0 24 24" aria-hidden="true"><g fill="none" stroke="#0d1b20" stroke-width="2"><circle cx="12" cy="12" r="9"/><ellipse cx="12" cy="12" rx="4" ry="9"/><path d="M3 12h18"/></g></svg>
        <span>www.brivoholdings.example</span>
      </p>
      <p class="contact-line">
        <span>@</span>
        <span>markdunthorpe@brivoholdings.example</span>
      </p>
    </div>
  </section>
</body>
</html>
```